TRU PEAK POWER.

I'd like my business logo.
contact name: Desmond Halvik
phone:0438275160
email: info@trupeakpower.net.au
website: www.trupeakpower.net.au

services:
solar
battery storage
LED lighting
energy saving solutions
general electrical
I'd like the design to look professional

Target Market(s)

Everyone

Industry/Entity Type

Business

Contact Information for Business Card

as described above

Requirements
Must have
• Id like the colours and the design to work well with my logo.

```html
<!DOCTYPE html>
<html lang="en">
<head>
<meta charset="utf-8">
<title>Tru Peak Power – Business Card</title>
<link rel="stylesheet" href="https://fonts.googleapis.com/css2?family=Arimo:wght@400;700&display=swap">
<style>
  :root {
    --page-bg: #2b2b2b;
    --green-dark: #3f9f36;
    --green-light: #7cc243;
    --green-text: #4caf3a;
    --orange: #f0a020;
    --ink: #1e1e1e;
    --ink-soft: #333333;
    --paper: #ffffff;
    --paper-shade: #eeeeee;
    --card-w: 600px;
    --card-h: 343px;
  }
  * { box-sizing: border-box; margin: 0; padding: 0; }
  html, body {
    width: 1200px; height: 997px; overflow: hidden;
    background: var(--page-bg);
    font-family: "Arimo", Arial, sans-serif;
  }
  .stage { position: relative; width: 1200px; height: 997px; }
  .card {
    position: absolute; left: 300px;
    width: var(--card-w); height: var(--card-h);
    border-radius: 22px; overflow: hidden;
  }

  /* Front */
  .card-front {
    top: 110px;
    background: linear-gradient(160deg, var(--green-dark) 0%, var(--green-light) 100%);
    color: var(--paper);
  }
  .service {
    position: absolute; font-size: 13px; letter-spacing: 1.5px;
    text-transform: uppercase; font-weight: 400; white-space: nowrap;
  }
  .service-battery { top: 60px; left: 50%; transform: translateX(-50%); }
  .service-solar   { top: 60px; right: 70px; }
  .service-led     { bottom: 70px; left: 60px; }
  .service-saving  { bottom: 70px; right: 80px; }
  .front-brand {
    position: absolute; top: 50%; left: 50%; transform: translate(-50%, -50%);
    display: flex; align-items: center; gap: 14px;
  }
  .brand-dot { width: 34px; height: 34px; border-radius: 50%; background: var(--paper); }
  .front-brand .brand-name {
    font-size: 34px; font-weight: 700; letter-spacing: 1px; color: var(--paper);
  }

  /* Back */
  .card-back {
    top: 530px;
    background: linear-gradient(160deg, var(--paper) 40%, var(--paper-shade) 100%);
  }
  .back-brand {
    position: absolute; top: 34px; right: 40px;
    display: flex; align-items: center; gap: 10px;
  }
  .back-brand .brand-dot { width: 26px; height: 26px; background: var(--orange); }
  .back-brand .brand-name {
    font-size: 24px; font-weight: 700; color: var(--green-text); letter-spacing: 0.5px;
  }
  .rule {
    position: absolute; top: 128px; left: 190px; right: 40px;
    height: 2px; background: var(--green-text);
  }
  .person { position: absolute; top: 112px; left: 50px; }
  .person-name { font-size: 18px; font-weight: 700; color: var(--green-text); }
  .person-role { font-size: 18px; color: var(--ink); margin-top: 2px; }
  .contact-list {
    position: absolute; left: 50px; top: 200px; list-style: none;
  }
  .contact-list li {
    display: flex; align-items: center; gap: 14px;
    font-size: 17px; color: var(--ink-soft); height: 36px;
  }
  .contact-list svg { width: 16px; height: 16px; fill: var(--green-text); }
  .mark-decoration {
    position: absolute; right: 60px; bottom: 70px;
    width: 120px; height: 120px; border-radius: 50%;
    background: radial-gradient(circle, rgba(124,194,67,0.35), rgba(240,160,32,0.25));
  }
</style>
</head>
<body>
<main class="stage">

  <section class="card card-front" aria-label="Business card front">
    <span class="service service-battery">Battery Storage</span>
    <span class="service service-solar">Solar</span>
    <div class="front-brand">
      <span class="brand-dot"></span>
      <span class="brand-name">TRU PEAK POWER</span>
    </div>
    <span class="service service-led">LED Lighting</span>
    <span class="service service-saving">Energy Saving Solutions</span>
  </section>

  <section class="card card-back" aria-label="Business card back">
    <div class="back-brand">
      <span class="brand-dot"></span>
      <span class="brand-name">TRU PEAK POWER</span>
    </div>
    <div class="rule"></div>
    <div class="person">
      <p class="person-name">Desmond Halvik</p>
      <p class="person-role">Director</p>
    </div>
    <ul class="contact-list">
      <li>
        <svg viewBox="0 0 16 16" aria-hidden="true"><path d="M3 1h3l1.5 4-2 1.2a9 9 0 0 0 4.3 4.3l1.2-2 4 1.5v3c0 1-1 2-2 2C6.5 15 1 9.5 1 3c0-1 1-2 2-2z"/></svg>
        <span>0438275160</span>
      </li>
      <li>
        <svg viewBox="0 0 16 16" aria-hidden="true"><path d="M1 3h14v10H1z M1 3l7 6 7-6" /></svg>
        <span>info@trupeakpower.net.au</span>
      </li>
      <li>
        <svg viewBox="0 0 16 16" aria-hidden="true"><circle cx="8" cy="8" r="7"/></svg>
        <span>www.trupeakpower.net.au</span>
      </li>
    </ul>
    <div class="mark-decoration" role="img" aria-label="Faint brand emblem decoration"></div>
  </section>

</main>
</body>
</html>
```